Menu sandwichbar

We have a sandwich bar and would like to change our menu.
The menu is a 3-panel folder with 6 printed sides.
We are looking for is original, quiet yet striking at the same time.
like black white newspaper style modern.

I have attached our current card. AND a screenshot with the style we want.

We have sandwiches, soup, pasta, pizza, salads and wraps.
So for each of these parts we need a breakdown.
I have also attached our logo.

We will need the file in EPS so we can add the dishes with the current price setting.

```html
<!DOCTYPE html>
<html lang="nl">
<head>
<meta charset="utf-8">
<title>Menu Sandwichbar</title>
<link rel="stylesheet" href="https://fonts.googleapis.com/css2?family=Bebas+Neue&family=Courier+Prime:wght@400;700&family=Roboto+Slab:wght@800&display=swap">
<style>
  :root {
    --ink: #1a1a1a;
    --paper: #ffffff;
    --red: #e31e24;
    --red-dark: #b3141a;
    --green: #8cb33a;
    --green-dark: #6e952a;
    --pill-outline: #d6d6d6;
    --pill-dark: #111111;
    --pill-mid: #3a3a3a;
    --pill-light: #b5b5b5;
    --art-fill: #ececec;
    --art-fill-2: #e2e2e2;
  }
  * { margin: 0; padding: 0; box-sizing: border-box; }
  html, body { width: 1200px; height: 848px; overflow: hidden; background: var(--paper); }
  .menu {
    position: relative; width: 1200px; height: 848px; overflow: hidden;
    background: linear-gradient(135deg, #ffffff 0%, #f6f6f6 50%, #ffffff 100%);
    font-family: "Courier Prime", "Courier New", monospace; color: var(--ink);
  }

  .header {
    position: absolute; border: 2px solid var(--pill-outline); border-radius: 40px;
    background: linear-gradient(100deg, #ffffff 55%, #cfcfcf 100%);
    padding: 8px 10px;
  }
  .header-bar {
    height: 100%; border-radius: 30px;
    background: linear-gradient(100deg, var(--pill-dark) 0%, var(--pill-mid) 56%, #7a7a7a 56.5%, var(--pill-light) 100%);
    box-shadow: 0 2px 3px rgba(0,0,0,.35);
    display: flex; align-items: center; justify-content: center; text-align: center;
    font-family: "Bebas Neue", Impact, sans-serif; color: #fff; font-size: 25px; line-height: 23px; letter-spacing: .5px;
  }

  .note {
    position: absolute; transform: translateX(-50%); text-align: center; white-space: nowrap;
    font-family: "Roboto Slab", Georgia, serif; font-weight: 800; font-size: 10.5px; line-height: 12px;
    color: var(--red); text-transform: uppercase; letter-spacing: .4px;
  }

  .row { position: absolute; white-space: nowrap; }
  .row .name { font-size: 13px; line-height: 16px; display: block; }
  .row .desc { font-size: 9px; line-height: 10.5px; display: block; }
  .row .price { position: absolute; top: 0; font-size: 13px; line-height: 16px; }

  .col-classic .row { left: 28px; } .col-classic .price { left: 296px; }
  .col-veggie .row { left: 418px; } .col-veggie .price { left: 319px; }
  .col-warm .row { left: 811px; } .col-warm .price { left: 295px; }
  .col-warm .desc { font-size: 8.6px; }
  .col-panini .row { left: 22px; } .col-panini .price { left: 307px; }
  .col-special .row { left: 408px; } .col-special .price { left: 330px; }
  .col-special .desc { font-size: 8.2px; }
  .col-soup .row { left: 137px; } .col-soup .price { left: 96px; }
  .col-pasta .row { left: 925px; } .col-pasta .price { left: 99px; }

  .art {
    position: absolute; border-radius: 6px;
    background: linear-gradient(180deg, var(--art-fill) 0%, var(--art-fill-2) 100%);
  }

  .ribbon { position: absolute; left: 0; top: 0; }
  .ribbon-label {
    position: absolute; transform: translate(-50%, -50%); white-space: nowrap;
    font-family: "Bebas Neue", Impact, sans-serif; font-size: 24px; color: #fff; letter-spacing: .5px;
  }
  .choice-list { position: absolute; font-size: 13px; line-height: 16px; }
</style>
</head>
<body>
<div class="menu">

  <!-- Traditionele broodjes zonder groenten -->
  <div class="header" style="left:20px; top:9px; width:363px; height:72px;">
    <div class="header-bar">Traditionele broodjes<br>zonder groenten</div>
  </div>
  <div class="note" style="left:204px; top:89px;">Standaard met boter<br>of mayonaise</div>
  <div class="art" role="img" aria-label="Illustratie van een olieflesje en een stuk kaas" style="left:168px; top:138px; width:130px; height:105px;"></div>

  <div class="col-classic">
    <div class="row" style="top:112px"><span class="name">Broodje Kaas</span><span class="price">€3,00</span></div>
    <div class="row" style="top:129px"><span class="name">Broodje Ham</span><span class="price">€3,00</span></div>
    <div class="row" style="top:146px"><span class="name">Broodje Salami</span><span class="price">€3,00</span></div>
    <div class="row" style="top:163px"><span class="name">Broodje Kaas En Ham</span><span class="price">€3,50</span></div>
    <div class="row" style="top:181px"><span class="name">Broodje Vleessla</span><span class="price">€3,50</span></div>
    <div class="row" style="top:198px"><span class="name">Broodje Eiersla</span><span class="price">€3,50</span></div>
    <div class="row" style="top:216px"><span class="name">Broodje Kip Hawai</span><span class="price">€3,50</span></div>
    <div class="row" style="top:232px"><span class="name">Broodje Kip Curry</span><span class="price">€3,50</span></div>
    <div class="row" style="top:249px"><span class="name">Broodje Kip Damourai</span><span class="price">€3,50</span></div>
    <div class="row" style="top:265px"><span class="name">Broodje Boulet Met</span><span class="desc">Mayonaise &amp; Curry Ketchup</span><span class="price">€3,50</span></div>
    <div class="row" style="top:294px"><span class="name">Broodje Préparé</span><span class="desc">Met Ui</span><span class="price">€3,50</span></div>
    <div class="row" style="top:322px"><span class="name">Broodje Martino</span><span class="desc">Metui &amp; Augurk</span><span class="price">€3,70</span></div>
    <div class="row" style="top:353px"><span class="name">Broodje Tonijnsla</span><span class="price">€3,70</span></div>
    <div class="row" style="top:369px"><span class="name">Broodje Krabsla</span><span class="price">€4,20</span></div>
    <div class="row" style="top:386px"><span class="name">Broodje Omelet Met Spek</span><span class="price">€4,20</span></div>
    <div class="row" style="top:401px"><span class="name">Broodje Brie</span><span class="desc">Methoning &amp; Nootjes</span><span class="price">€4,20</span></div>
    <div class="row" style="top:431px"><span class="name">Broodje Gerookte Zalm</span><span class="desc">Met Ui</span><span class="price">€4,70</span></div>
  </div>

  <!-- Traditionele broodjes met groenten -->
  <div class="header" style="left:415px; top:9px; width:364px; height:72px;">
    <div class="header-bar">Traditionele broodjes<br>met groenten</div>
  </div>
  <div class="note" style="left:599px; top:89px;">Standaard metsla, tomaat,<br>komkommer, ei &amp; mayonaise</div>
  <div class="art" role="img" aria-label="Illustratie van een belegd stokbrood met sla en tomaat" style="left:566px; top:212px; width:140px; height:108px;"></div>

  <div class="col-veggie">
    <div class="row" style="top:114px"><span class="name">Smos Kaas</span><span class="price">€3,70</span></div>
    <div class="row" style="top:131px"><span class="name">Smos Ham</span><span class="price">€3,70</span></div>
    <div class="row" style="top:147px"><span class="name">Smos Salami</span><span class="price">€3,70</span></div>
    <div class="row" style="top:164px"><span class="name">Smos Kaas En Ham</span><span class="price">€4,00</span></div>
    <div class="row" style="top:180px"><span class="name">Smos Vleessla</span><span class="price">€4,00</span></div>
    <div class="row" style="top:197px"><span class="name">Smos Eiersla</span><span class="price">€4,00</span></div>
    <div class="row" style="top:213px"><span class="name">Smos Kip Hawai</span><span class="price">€4,00</span></div>
    <div class="row" style="top:230px"><span class="name">Smos Kip Curry</span><span class="price">€4,00</span></div>
    <div class="row" style="top:246px"><span class="name">Smos Kip Samourai</span><span class="price">€4,00</span></div>
    <div class="row" style="top:263px"><span class="name">Smos Boulet Met</span><span class="desc">Mayonaise &amp; Curry Ketchup</span><span class="price">€4,00</span></div>
    <div class="row" style="top:290px"><span class="name">Smos Préparé</span><span class="desc">Met Ui</span><span class="price">€4,00</span></div>
    <div class="row" style="top:317px"><span class="name">Smos Martino</span><span class="desc">Met Ui &amp; Augurk</span><span class="price">€4,00</span></div>
    <div class="row" style="top:344px"><span class="name">Smos Tonijnsla</span><span class="price">€4,00</span></div>
    <div class="row" style="top:359px"><span class="name">Smos Krabsla</span><span class="price">€4,70</span></div>
    <div class="row" style="top:374px"><span class="name">Smos Omelet Met Spek</span><span class="price">€4,70</span></div>
    <div class="row" style="top:389px"><span class="name">Smos Gerookte Zalm</span><span class="desc">Met Ui</span><span class="price">€5,20</span></div>
    <div class="row" style="top:414px"><span class="name">Smos Begetarisch</span><span class="price">€4,00</span></div>
  </div>

  <!-- Warme broodjes -->
  <div class="header" style="left:874px; top:21px; width:240px; height:47px; padding:5px 7px;">
    <div class="header-bar">Warme broodjes</div>
  </div>
  <div class="art" role="img" aria-label="Illustratie van een hamburger" style="left:956px; top:91px; width:105px; height:84px;"></div>

  <div class="col-warm">
    <div class="row" style="top:105px"><span class="name">Crispy Burger</span><span class="price">€3,10</span></div>
    <div class="row" style="top:123px"><span class="name">Crispy Cheese</span><span class="price">€3,20</span></div>
    <div class="row" style="top:142px"><span class="name">Crispy Royal</span><span class="price">€4,20</span></div>
    <div class="row" style="top:159px"><span class="name">Crispy Beef</span><span class="price">€4,20</span></div>
    <div class="row" style="top:179px"><span class="name">Smos Warme Boulet</span><span class="desc">Boulet, Standaard Salade, Curry Ketchup &amp; Mayonaise</span><span class="price">€4,10</span></div>
    <div class="row" style="top:205px"><span class="name">Smos Mexicano</span><span class="price">€4,60</span></div>
    <div class="row" style="top:222px"><span class="name">Smos Kip Krokant</span><span class="price">€4,60</span></div>
    <div class="row" style="top:240px"><span class="name">Warm Broodje Roadhouse</span><span class="desc">Pikante kipreepjes, sla, ui, frieten &amp; barbequesaus</span><span class="price">€5,20</span></div>
    <div class="row" style="top:271px"><span class="name">Smos Bommeke</span><span class="desc">Platte hamburger, frieten, sla, tomaat &amp; mayonaise</span><span class="price">€5,20</span></div>
    <div class="row" style="top:300px"><span class="name">Broodje Warme Fishburger</span><span class="desc">Fishburger, sla, tomaat, frieten &amp; tartaarsaus</span><span class="price">€5,20</span></div>
    <div class="row" style="top:332px"><span class="name">Bourgondiër</span><span class="desc">Brie, gebakken spek,&nbsp; honing &amp; nootjes</span><span class="price">€5,50</span></div>
  </div>

  <!-- Pasta in the box -->
  <div class="header" style="left:874px; top:392px; width:240px; height:47px; padding:5px 7px;">
    <div class="header-bar">Pasta in the box</div>
  </div>
  <div class="col-pasta">
    <div class="row" style="top:456px"><span class="name">Small</span><span class="price">€5,00</span></div>
    <div class="row" style="top:472px"><span class="name">Medium</span><span class="price">€6,00</span></div>
    <div class="row" style="top:487px"><span class="name">Large</span><span class="price">€7,00</span></div>
  </div>
  <div class="art" role="img" aria-label="Illustratie van een bord spaghetti met tomaatjes en basilicum" style="left:809px; top:510px; width:165px; height:91px;"></div>

  <svg class="ribbon" width="1200" height="848" viewBox="0 0 1200 848" aria-hidden="true">
    <polygon points="1175,567 1200,548 1200,590 1175,606" fill="var(--green-dark)"/>
    <polygon points="998,587 1010,567 1175,567 1175,606 1010,606" fill="var(--green)"/>
    <polygon points="798,704 825,724 825,762 798,740" fill="var(--red-dark)"/>
    <polygon points="825,724 1063,724 1074,743 1063,762 825,762" fill="var(--red)"/>
  </svg>
  <div class="ribbon-label" style="left:1086px; top:589px;">Kies je pasta</div>
  <div class="ribbon-label" style="left:942px; top:744px;">Kies je saus &amp; je topping</div>

  <div class="art" role="img" aria-label="Illustratie van fusilli, penne en conchiglie" style="left:847px; top:632px; width:279px; height:55px;"></div>

  <div class="choice-list" style="left:834px; top:777px;">Bolognaise<br>Carbonara<br>Kipgehakt&amp;prei</div>
  <div class="choice-list" style="left:989px; top:777px;">Parmesan<br>Gruyère<br>Peterselie</div>
  <div class="art" role="img" aria-label="Illustratie van een vork met spaghetti" style="left:1097px; top:713px; width:103px; height:128px;"></div>

  <!-- Soepen -->
  <div class="header" style="left:82px; top:461px; width:239px; height:47px; padding:5px 7px;">
    <div class="header-bar">Soepen</div>
  </div>
  <div class="note" style="left:208px; top:518px;">Dagsoep of tomatensoep</div>
  <div class="art" role="img" aria-label="Illustratie van een kom tomatensoep op een bordje" style="left:10px; top:523px; width:110px; height:73px;"></div>
  <div class="col-soup">
    <div class="row" style="top:538px"><span class="name">1 Tas</span><span class="price">€2,00</span></div>
    <div class="row" style="top:553px"><span class="name">1L Soep</span><span class="price">€3,00</span></div>
  </div>

  <!-- Panini's -->
  <div class="header" style="left:82px; top:610px; width:239px; height:47px; padding:5px 7px;">
    <div class="header-bar">Panini's</div>
  </div>
  <div class="art" role="img" aria-label="Illustratie van een belegde panini" style="left:192px; top:674px; width:122px; height:63px;"></div>
  <div class="col-panini">
    <div class="row" style="top:679px"><span class="name">Panini kaas &amp; ham</span><span class="price">€3,50</span></div>
    <div class="row" style="top:696px"><span class="name">Panini traditioneel</span><span class="desc">Mozzarella, basilicum &amp; tomaat</span><span class="price">€4,60</span></div>
    <div class="row" style="top:725px"><span class="name">Panini parma</span><span class="desc">Mozzarella, basilicum, parmaham &amp; tomaat</span><span class="price">€5,00</span></div>
    <div class="row" style="top:753px"><span class="name">Panini brie</span><span class="desc">Brie, honing &amp; nootjes</span><span class="price">€5,00</span></div>
    <div class="row" style="top:781px"><span class="name">Panini kip</span><span class="desc">Kip, mozzarella, ananas &amp; rucola</span><span class="price">€5,20</span></div>
    <div class="row" style="top:812px"><span class="name">Panini boulet</span><span class="desc">Boulet, mozzarella, tomaat &amp; black pepersaus</span><span class="price">€5,20</span></div>
  </div>

  <!-- Speciale broodjes -->
  <div class="header" style="left:477px; top:454px; width:240px; height:47px; padding:5px 7px;">
    <div class="header-bar">Speciale broodjes</div>
  </div>
  <div class="art" role="img" aria-label="Illustratie van tomaten aan de tros" style="left:729px; top:452px; width:52px; height:45px;"></div>
  <div class="col-special">
    <div class="row" style="top:519px"><span class="name">Boulet Special</span><span class="desc">Boulet, Aardappelsla, Mayonaise, Ketchup &amp; Standaard Salade</span><span class="price">€4,70</span></div>
    <div class="row" style="top:546px"><span class="name">Smos Special</span><span class="desc">Kaas, Ham, Aardappelsla, Mayonaise &amp; Standaard Salade</span><span class="price">€4,70</span></div>
    <div class="row" style="top:574px"><span class="name">Smos Brie</span><span class="desc">Brie, Honing, Nootjes &amp; Standaard Salade</span><span class="price">€4,70</span></div>
    <div class="row" style="top:601px"><span class="name">Roadhouse Special</span><span class="desc">Gepluisde Kip, Barbecue saus, Ananas &amp; Standaard Salade</span><span class="price">€4,70</span></div>
    <div class="row" style="top:630px"><span class="name">Mozzarella</span><span class="desc">Mozzarella, Rucola, Zongedroogde Tomaten &amp; Basilicum</span><span class="price">€4,70</span></div>
    <div class="row" style="top:658px"><span class="name">Zalm Special</span><span class="desc">Alpi Kruidenkaas, Gerookte Zalm, Ui, Dressing &amp; standaard Salade</span><span class="price">€5,20</span></div>
    <div class="row" style="top:686px"><span class="name">Basilicum</span><span class="desc">Italiaanse Ham, Mozzarella, Rucola, Zongedroogde Tomaat &amp;<br>Basilicum</span><span class="price">€5,20</span></div>
    <div class="row" style="top:725px"><span class="name">Italiaans Festijn</span><span class="desc">Olijfolie, Parmaham, Rucola, Pijnboompitten, Parmazaanse Kaas,<br>Tomaat &amp; Peper En Zout</span><span class="price">€5,50</span></div>
    <div class="row" style="top:766px"><span class="name">Surf &amp; Turf</span><span class="desc">Tonijnsla, Rosbief, Kappertjes, Rucola, Verse Tomaten</span><span class="price">€5,50</span></div>
    <div class="row" style="top:797px"><span class="name">Tagliata</span><span class="desc">Rosbief, Balsamico azijn, Olijfolie, Parmezaan Schilfers, Rucola,<br>Zongedroogde Tomaten</span><span class="price">€5,50</span></div>
  </div>

</div>
</body>
</html>
```